Website Landing Page for Marlowe Systems

Create a custom designed website landing page for our business. Looking for a professional upscale design that incorporates our logo and logo colors into the theme. I want a standard fixed frame website, not a constant scrolling format that seems to be the trend. To start with I'm looking for more of the graphic design part, maybe a concept or theme, I don't expect to see a finished project. Not interested in generic templates or layouts.

The name of our company is Marlowe Systems and I've attached our logo below. I'd like to have the web page have the same look and feel of our logo, as well as the colors. Our company, Marlowe Systems does system design, installation, and programming, of residential and commercial Audio/Video and Automation systems. We do home theaters, lighting and building automation, video conferencing systems, security camera installations, conference rooms, projectors, distributed audio systems, and similar Technology projects. This will be a professional services/informational website. We will not sell products on this website. This website will be used to advertise our company and communicate our services to prospective customers. Having a well designed, professional and clean website is one way we want to distinguish our company from the competition.

Here are some examples of what I consider a professional well designed website
http://www.qrzstudio.example/Work/

Last year we had our tradeloft store designed (with PixelHarbor) and I'm really happy with the way it turned out. You can see it at www.KelpGearDepot.example I consider this to be a great design and looking for the same level of quality with this new website. However, do not copy or use any part of this design in this new project. This tradeloft store is completely separate from our other company Marlowe Systems. I only mention this tradeloft store an an example of good work.

Target Market(s)

People interested in Audio/Video, home theaters, home automation. We do sales, system design, and programming. We typically work on larger projects with both residential and commercial customers.

Industry/Entity Type

Business

Number of Pages Required

1 page

Requirements
Must have
• Great design elements. Please use a white background. I think white goes well with our logo colors.

```html
<!DOCTYPE html>
<html lang="en">
<head>
<meta charset="utf-8">
<title>Marlowe Systems – Ask for a Quote</title>
<link rel="stylesheet" href="https://fonts.googleapis.com/css2?family=Roboto+Condensed:wght@400;700&family=Roboto:wght@400&display=swap">
<style>
  :root {
    --brand-green: #7cc242;
    --brand-blue: #3a8fd0;
    --brand-blue-dark: #2f7fc0;
    --white: #ffffff;
    --label-grey: #6a6a6a;
    --field-border: #8a8a8a;
  }
  * { box-sizing: border-box; margin: 0; padding: 0; }
  html, body {
    width: 1200px;
    height: 675px;
    overflow: hidden;
    background: var(--white);
  }
  .stage {
    position: relative;
    width: 1366px;
    height: 768px;
    transform: scale(0.878477);
    transform-origin: 0 0;
    background: var(--white);
    font-family: "Roboto", Arial, sans-serif;
  }
  .backdrop {
    position: absolute;
    inset: 0;
  }
  .brand {
    position: absolute;
    left: 31px;
    top: 29px;
    display: flex;
    align-items: center;
    gap: 26px;
  }
  .brand__mark {
    width: 114px;
    height: 114px;
    border-radius: 50%;
    border: 9px solid var(--brand-blue);
  }
  .brand__name {
    font-family: "Roboto Condensed", Arial, sans-serif;
    font-weight: 400;
    font-size: 36px;
    line-height: 1.05;
    letter-spacing: 1px;
    color: var(--brand-blue);
    text-transform: uppercase;
  }
  .quote-card {
    position: absolute;
    left: 867px;
    top: 328px;
    width: 435px;
    height: 369px;
    background: var(--white);
    box-shadow: 0 4px 14px rgba(0,0,0,0.35);
  }
  .quote-card__title {
    position: absolute;
    top: 10px;
    left: 0;
    width: 100%;
    text-align: center;
    font-family: "Roboto Condensed", Arial, sans-serif;
    font-weight: 700;
    font-size: 33px;
    color: var(--brand-blue);
  }
  .field {
    position: absolute;
    left: 53px;
    width: 356px;
  }
  .field__label {
    display: block;
    font-size: 15px;
    color: var(--label-grey);
    margin-bottom: 10px;
  }
  .field__input {
    display: block;
    width: 356px;
    height: 31px;
    border: 1px solid var(--field-border);
    background: var(--white);
  }
  .field--name { top: 76px; }
  .field--email { top: 158px; left: 52px; }
  .field--phone { top: 227px; left: 54px; width: 355px; }
  .field--phone .field__input { width: 355px; }
  .quote-card__button {
    position: absolute;
    left: 115px;
    top: 309px;
    width: 233px;
    height: 31px;
    border: none;
    background: linear-gradient(#4aa3df, var(--brand-blue-dark));
    color: var(--white);
    font-family: "Roboto Condensed", Arial, sans-serif;
    font-weight: 700;
    font-size: 20px;
  }
  .site-footer {
    position: absolute;
    left: 0;
    top: 740px;
    width: 1366px;
    height: 28px;
    background: var(--brand-green);
    color: var(--white);
    font-family: "Roboto Condensed", Arial, sans-serif;
    font-size: 19px;
    line-height: 28px;
    text-align: center;
    text-transform: uppercase;
    white-space: pre;
  }
</style>
</head>
<body>
<div class="stage">
  <svg class="backdrop" viewBox="0 0 1366 768" width="1366" height="768">
    <defs>
      <linearGradient id="lounge-tones" x1="0" y1="145" x2="0" y2="740" gradientUnits="userSpaceOnUse">
        <stop offset="0" stop-color="#d9c392"/>
        <stop offset="0.12" stop-color="#f0d99a"/>
        <stop offset="0.25" stop-color="#f1ebdc"/>
        <stop offset="0.42" stop-color="#6f8a55"/>
        <stop offset="0.58" stop-color="#e9e2d0"/>
        <stop offset="0.72" stop-color="#5e3f2d"/>
        <stop offset="0.84" stop-color="#3e322b"/>
        <stop offset="0.92" stop-color="#b8a48a"/>
        <stop offset="1" stop-color="#d8cfc0"/>
      </linearGradient>
      <linearGradient id="restaurant-tones" x1="235" y1="60" x2="1100" y2="300" gradientUnits="userSpaceOnUse">
        <stop offset="0" stop-color="#2c221e"/>
        <stop offset="0.25" stop-color="#5a3a28"/>
        <stop offset="0.45" stop-color="#9a6238"/>
        <stop offset="0.6" stop-color="#c9c9c6"/>
        <stop offset="0.75" stop-color="#3d4246"/>
        <stop offset="1" stop-color="#6f8a86"/>
      </linearGradient>
      <linearGradient id="tower-tones" x1="1366" y1="0" x2="700" y2="740" gradientUnits="userSpaceOnUse">
        <stop offset="0" stop-color="#2a63c4"/>
        <stop offset="0.3" stop-color="#5f8fd2"/>
        <stop offset="0.5" stop-color="#e6ebf1"/>
        <stop offset="0.7" stop-color="#8fb1d9"/>
        <stop offset="1" stop-color="#6b8fbf"/>
      </linearGradient>
    </defs>
    <g role="img" aria-label="Photo of a restaurant bar interior with wood floor, pendant lights and bar stools">
      <polygon points="235,245 600,0 1366,0 668,428" fill="url(#restaurant-tones)"/>
    </g>
    <g role="img" aria-label="Photo of a living room with a large wall screen, speakers, cabinets and sofa">
      <polygon points="0,145 668,428 668,740 0,740" fill="url(#lounge-tones)"/>
    </g>
    <g role="img" aria-label="Photo of a glass office building against a blue sky">
      <polygon points="668,428 1366,0 1366,740 668,740" fill="url(#tower-tones)"/>
    </g>
    <g class="divider-lines" stroke="#7cc242" stroke-width="7" fill="none">
      <line x1="-5" y1="143" x2="670" y2="430"/>
      <line x1="235" y1="245" x2="604" y2="-3"/>
      <line x1="666" y1="431" x2="1370" y2="-2"/>
      <line x1="670" y1="428" x2="670" y2="742"/>
    </g>
  </svg>

  <div class="brand">
    <div class="brand__mark"></div>
    <div class="brand__name">Marlowe<br>Systems</div>
  </div>

  <form class="quote-card">
    <h1 class="quote-card__title">ASK FOR A QUOTE</h1>
    <label class="field field--name"><span class="field__label">Your name</span><span class="field__input"></span></label>
    <label class="field field--email"><span class="field__label">Email address</span><span class="field__input"></span></label>
    <label class="field field--phone"><span class="field__label">Phone number</span><span class="field__input"></span></label>
    <button type="button" class="quote-card__button">Send me a Quote</button>
  </form>

  <footer class="site-footer">@Marlowe Systems 2017          |          All rights reserved</footer>
</div>
</body>
</html>
```